Quiet Harbor Hours Podcast Artwork

I need a cover for my podcast Quiet Harbor Hours that is clean, modern, and minimalist, but not too feminine

Target Market(s)

People struggling with fertility particularly women who are between the ages of 35-45 though there is a small set of listeners who are men

Requirements
Must have
• Embryo in the Zero
Should not have
• No script text

```html
<!DOCTYPE html>
<html lang="en">
<head>
<meta charset="utf-8">
<title>Quiet Harbor Hours – Podcast Cover</title>
<link rel="stylesheet" href="https://fonts.googleapis.com/css2?family=Playfair+Display:wght@400;500&display=swap">
<style>
  :root {
    --page: #eef0ec;
    --sage: #a0ae8b;
    --blush: #f7e0d6;
    --white: #ffffff;
    --earth-dark: #6b5336;
    --earth-mid: #a58a66;
  }
  * { margin: 0; padding: 0; box-sizing: border-box; }
  html, body {
    width: 1200px;
    height: 898px;
    overflow: hidden;
    background: var(--page);
  }
  .canvas {
    position: relative;
    width: 1200px;
    height: 898px;
  }
  .cover {
    position: absolute;
    left: 170px;
    top: 19px;
    width: 860px;
    height: 860px;
    background: var(--sage);
    overflow: hidden;
    font-family: "Playfair Display", Georgia, serif;
  }
  .title-top {
    position: absolute;
    left: 52px;
    top: 30px;
    color: var(--white);
    font-size: 250px;
    font-weight: 500;
    line-height: 1;
    letter-spacing: -4px;
  }
  .accent-dot {
    position: absolute;
    left: 693px;
    top: 138px;
    width: 148px;
    height: 148px;
    border-radius: 50%;
    background: var(--blush);
  }
  .title-bottom {
    position: absolute;
    left: 0;
    width: 100%;
    top: 345px;
    text-align: center;
    color: var(--blush);
    font-size: 122px;
    font-weight: 400;
    line-height: 1;
    letter-spacing: -1px;
  }
  .earth {
    position: absolute;
    left: 0;
    bottom: 0;
    width: 860px;
    height: 320px;
    display: block;
  }
</style>
</head>
<body>
<div class="canvas">
  <section class="cover">
    <div class="title-top">Quiet</div>
    <div class="accent-dot"></div>
    <h1 class="title-bottom">Harbor Hours</h1>
    <svg class="earth" viewBox="0 0 860 320" role="img" aria-label="Photograph of cracked dry earth with a torn paper edge">
      <defs>
        <linearGradient id="earthTone" x1="0" y1="0" x2="1" y2="1">
          <stop offset="0" stop-color="#f3eee7"/>
          <stop offset="0.5" stop-color="#e6dccd"/>
          <stop offset="1" stop-color="#efe8de"/>
        </linearGradient>
      </defs>
      <polygon fill="url(#earthTone)"
        points="0,50 30,40 60,45 95,32 130,36 160,28 200,38 235,44 270,40 300,46 340,42 380,50 410,44 440,46 470,38 500,40 530,30 555,20 580,22 600,10 625,14 650,8 680,18 700,24 730,22 760,30 790,26 820,34 860,32 860,320 0,320"/>
    </svg>
  </section>
</div>
</body>
</html>
```